Profesional personal website needs design and business card

I need a business card with my professional name as a logo "Marlo Vitality" for my business. I am a Wellness Coach, consultant and trainer. So it should be professional, wellness oriented and modern.

Target Market(s)

Private clients, governments, corporations. Luxury and high market.

Industry/Entity Type

Health And Wellness

Contact Information for Business Card

Marlo Vitality should be the logo

Colors

Designer to choose colors to be used in the design.

Requirements
Must have
• Marlo Vitality
• Name: Tomás Arribal
• Wellness Coach, Consultant & Trainer.
• Website: www.marlovitality.example
• Phone:
• Spain (+34) 612 480 397
• (USA) +1 (555) 318 2046
Nice to have
• The most important is the design of "Marlo Vitality", as this is going to be my personal brand logo. It should be professional, wellness, high end and actual.
Should not have
• no golds, no baroque style..

```html
<!DOCTYPE html>
<html lang="en">
<head>
<meta charset="utf-8">
<title>Marlo Vitality – Business Card</title>
<link rel="stylesheet" href="https://fonts.googleapis.com/css2?family=Raleway:wght@400;500;600&display=swap">
<style>
  :root {
    --backdrop: #3b3b39;
    --card-dark: #141416;
    --card-light: #f3f3f2;
    --brand-blue: #2f8fd0;
    --text-grey: #5e6063;
    --text-dark: #3c3d40;
    --logo-grey: #8d8f92;
  }
  * { box-sizing: border-box; margin: 0; padding: 0; }
  html, body {
    width: 1200px; height: 824px; overflow: hidden;
    background: var(--backdrop);
    font-family: "Raleway", Arial, sans-serif;
  }
  .stage {
    position: relative; width: 1200px; height: 824px;
  }
  .card {
    position: absolute; top: 262px;
    width: 520px; height: 300px;
    border-radius: 3px;
    box-shadow: 0 10px 28px rgba(0,0,0,.45);
  }
  .card--front { left: 50px; background: var(--card-dark); }
  .card--back  { left: 630px; background: var(--card-light); }

  .wordmark {
    position: absolute;
    display: flex; align-items: center; gap: 12px;
    font-weight: 500; letter-spacing: .5px;
    white-space: nowrap;
  }
  .wordmark__dot {
    width: 22px; height: 22px; border-radius: 50%;
    background: var(--brand-blue);
  }
  .card--front .wordmark {
    left: 50%; top: 50%; transform: translate(-50%, -50%);
    font-size: 44px; color: var(--logo-grey);
  }
  .card--back .wordmark {
    left: 34px; top: 112px;
    font-size: 30px; color: var(--text-grey);
    gap: 9px;
  }
  .card--back .wordmark__dot { width: 16px; height: 16px; }

  .contact {
    position: absolute; left: 300px; top: 118px;
    color: var(--text-dark);
  }
  .contact__name {
    font-size: 22px; font-weight: 500; color: var(--text-grey);
    letter-spacing: .3px;
  }
  .contact__role {
    font-size: 11.5px; font-weight: 500; color: var(--brand-blue);
    margin: 3px 0 12px;
  }
  .contact__list { list-style: none; }
  .contact__item {
    display: flex; align-items: center; gap: 8px;
    font-size: 12.5px; line-height: 21px;
  }
  .contact__icon { width: 12px; height: 12px; fill: var(--brand-blue); flex: none; }
</style>
</head>
<body>
<main class="stage">
  <section class="card card--front" aria-label="Business card front">
    <div class="wordmark">
      <span class="wordmark__dot"></span>
      <span class="wordmark__name">Marlo Vitality</span>
    </div>
  </section>

  <section class="card card--back" aria-label="Business card back">
    <div class="wordmark">
      <span class="wordmark__dot"></span>
      <span class="wordmark__name">Marlo Vitality</span>
    </div>

    <div class="contact">
      <p class="contact__name">Tomás Arribal</p>
      <p class="contact__role">Wellness Coach, Consultant &amp; Trainer</p>
      <ul class="contact__list">
        <li class="contact__item">
          <svg class="contact__icon" viewBox="0 0 24 24"><path d="M6.6 10.8a15.1 15.1 0 0 0 6.6 6.6l2.2-2.2c.3-.3.7-.4 1-.2 1.1.4 2.3.6 3.6.6.6 0 1 .4 1 1V20c0 .6-.4 1-1 1A17 17 0 0 1 3 4c0-.6.4-1 1-1h3.5c.6 0 1 .4 1 1 0 1.3.2 2.5.6 3.6.1.3 0 .7-.2 1z"/></svg>
          <span>Spain (+34) 612 480 397</span>
        </li>
        <li class="contact__item">
          <svg class="contact__icon" viewBox="0 0 24 24"><path d="M6.6 10.8a15.1 15.1 0 0 0 6.6 6.6l2.2-2.2c.3-.3.7-.4 1-.2 1.1.4 2.3.6 3.6.6.6 0 1 .4 1 1V20c0 .6-.4 1-1 1A17 17 0 0 1 3 4c0-.6.4-1 1-1h3.5c.6 0 1 .4 1 1 0 1.3.2 2.5.6 3.6.1.3 0 .7-.2 1z"/></svg>
          <span>(USA) +1 (555) 318 2046</span>
        </li>
        <li class="contact__item">
          <svg class="contact__icon" viewBox="0 0 24 24"><path d="M12 2a10 10 0 1 0 0 20 10 10 0 0 0 0-20zm6.9 6h-2.9a15.7 15.7 0 0 0-1.4-3.6A8 8 0 0 1 18.9 8zM12 4c.8 1.2 1.5 2.5 1.9 4h-3.8c.4-1.5 1.1-2.8 1.9-4zM4.3 14a8.2 8.2 0 0 1 0-4h3.4a16.5 16.5 0 0 0 0 4zm.8 2h2.9c.3 1.3.8 2.5 1.4 3.6A8 8 0 0 1 5.1 16zM8 8H5.1a8 8 0 0 1 4.3-3.6C8.8 5.5 8.3 6.7 8 8zm4 12c-.8-1.2-1.5-2.5-1.9-4h3.8c-.4 1.5-1.1 2.8-1.9 4zm2.3-6H9.7a14.7 14.7 0 0 1 0-4h4.6a14.7 14.7 0 0 1 0 4zm.3 5.6c.6-1.1 1.1-2.3 1.4-3.6h2.9a8 8 0 0 1-4.3 3.6zm1.7-5.6a16.5 16.5 0 0 0 0-4h3.4a8.2 8.2 0 0 1 0 4z"/></svg>
          <span>www.marlovitality.example</span>
        </li>
      </ul>
    </div>
  </section>
</main>
</body>
</html>
```